Copperfox Billboard

Please design a billboard using my photos and logos.
For photo of truck please crop the truck itself out and not have the trees / dirt in photo.
Please put " Best Prices in Sevier County"
Please put " 30-yard Dumpsters Starting at 600.00"
Please put " 16-yard Dumpsters Starting at 300.0"
Please put " Delivery and Pickup 7 Days a week"
Billboard size will be 10 ft tall 30 ft wide

```html
<!DOCTYPE html>
<html lang="en">
<head>
<meta charset="utf-8">
<title>Copperfox Dumpsters Billboard</title>
<link rel="stylesheet" href="https://fonts.googleapis.com/css2?family=Exo+2:ital,wght@0,800;1,800;1,900&display=swap">
<style>
  :root {
    --purple: #7b3f9e;
    --purple-soft: #8a52ad;
    --ink: #0b0b0d;
    --ink-2: #1c1c20;
    --white: #ffffff;
    --page: #d9d9db;
  }
  * { box-sizing: border-box; margin: 0; padding: 0; }
  html, body { width: 1198px; height: 1200px; overflow: hidden; }
  body {
    background: var(--page);
    font-family: "Exo 2", sans-serif;
    position: relative;
  }
  .billboard {
    position: absolute;
    left: 49px; top: 423px;
    width: 1100px; height: 354px;
    background: radial-gradient(ellipse at 60% 40%, var(--ink-2) 0%, var(--ink) 70%);
    box-shadow: 0 6px 14px rgba(0,0,0,0.25);
    overflow: hidden;
    color: var(--white);
  }
  .brand {
    position: absolute;
    left: 41px; top: 30px;
    width: 354px;
    font-weight: 800;
    color: var(--white);
    text-transform: uppercase;
    line-height: 1;
  }
  .brand-name { display: block; font-size: 62px; letter-spacing: 1px; }
  .brand-trade { display: block; font-size: 34px; text-align: right; margin-top: 6px; letter-spacing: 1px; }
  .offer-line {
    position: absolute;
    left: 41px;
    line-height: 1;
    font-style: italic;
    font-weight: 900;
    text-transform: uppercase;
    letter-spacing: 2px;
    white-space: nowrap;
  }
  .accent { color: var(--purple-soft); }
  .tagline { top: 159px; font-size: 22px; }
  .size-large { font-size: 23px; }
  .size-small { font-size: 21px; }
  .divider {
    position: absolute; left: 41px;
    height: 1.5px; background: var(--purple);
  }
  .band {
    position: absolute;
    left: 0; bottom: 0;
    width: 100%; height: 41px;
    background: var(--purple);
  }
  .band-text {
    position: absolute;
    left: 41px; top: 9px;
    line-height: 1;
    font-style: italic; font-weight: 900;
    font-size: 22px; letter-spacing: 2px;
    text-transform: uppercase;
    white-space: nowrap;
  }
  .phone {
    position: absolute;
    right: 45px; top: 4px;
    line-height: 1;
    font-style: italic; font-weight: 900;
    font-size: 33px; letter-spacing: 1px;
    white-space: nowrap;
  }
  .truck-disc {
    position: absolute;
    left: 602px; top: 211px;
    width: 130px; height: 130px;
    border-radius: 50%;
    background: var(--ink);
  }
  .truck-photo {
    position: absolute;
    left: 478px; top: 36px;
    width: 546px; height: 270px;
    border-radius: 40px 24px 24px 60px;
    background: linear-gradient(100deg, #f2f2f2 0%, #cfcfd3 45%, #4a2a68 70%, #3a1f58 100%);
  }
</style>
</head>
<body>
  <section class="billboard">
    <div class="brand">
      <span class="brand-name">Copperfox</span>
      <span class="brand-trade">Dumpsters</span>
    </div>

    <p class="offer-line tagline">Best Prices in Sevier County</p>
    <div class="divider" style="top:186px; width:300px;"></div>

    <p class="offer-line size-large" style="top:196px;"><span class="accent">30-Yard</span> Dumpsters</p>
    <p class="offer-line size-large" style="top:221px;">Starting at <span class="accent">600.00</span></p>
    <div class="divider" style="top:249px; width:240px;"></div>

    <p class="offer-line size-small" style="top:257px;"><span class="accent">16-Yard</span> Dumpsters</p>
    <p class="offer-line size-small" style="top:281px;">Starting at <span class="accent">300.0</span></p>

    <div class="band">
      <p class="band-text">Delivery and Pickup 7 Days a Week</p>
      <p class="phone">123-456-7890</p>
    </div>

    <div class="truck-disc"></div>
    <div class="truck-photo" role="img" aria-label="Photo of a white roll-off truck carrying a purple dumpster container, cut out from its background"></div>
  </section>
</body>
</html>
```